(サイズ)W1000×H2000
(詳細)音楽療育に特化した放課後等デイサービス事業所の、ガラス面のシートです。看板も兼ねておりますので、事業所名を伝えることが第一です。音楽のイメージで、かつ児童が通う施設なので、どちらかというと児童向け(かわいらしい)イメージが良いです。
記載項目
添付資料はイメージです。以下項目を入れていただきたいと思います。

※必ず入れていただきたい項目
(事業名)
放課後等デイサービス
児童発達支援
(事業所名)
星のクルミ
(電話番号)
048-372-9051

※その他文言は特に必要としていませんが、こんな表現があれば、等あれば添付資料を参考に入れていただいても問題ありません。

青系、緑系、青系、または緑系どちらかが良いです。
(サイズ変更)
W1272×H1800に変更をお願い申し上げます。

事業所スタッフの多数決で決めました。明るい雰囲気がとても良かったです。

とても良い提案をたくさん頂きありがとうございました。大変悩みましたが、多数決で選定させていただきました。またパンフ等でお願いする予定ですが、宜しくお願い致します。

```html
<!DOCTYPE html>
<html lang="ja">
<head>
<meta charset="UTF-8">
<title>星のクルミ ウィンドウサイン</title>
<link rel="stylesheet" href="https://fonts.googleapis.com/css2?family=M+PLUS+Rounded+1c:wght@700;800;900&display=swap">
<style>
  :root {
    --sky-deep: #a9c6ea;
    --sky-soft: #dfe9f7;
    --paper: #f8fbff;
    --leaf: #3f9b2f;
    --leaf-dark: #2e7f22;
    --leaf-glow: #b8ec8a;
    --cloud: #3f8fd8;
    --cloud-light: #7fbdf0;
    --tag: #2f9a38;
    --phone: #ffffff;
    --phone-edge: #4a82d6;
    --blossom: #f6a9c7;
    --note-pink: #ee4f97;
    --illust-warm: #f4c64a;
    --illust-cool: #7fa3dd;
  }
  html, body {
    margin: 0;
    padding: 0;
    overflow: hidden;
  }
  body {
    width: 851px;
    height: 1200px;
    font-family: "M PLUS Rounded 1c", sans-serif;
  }
  .sign {
    position: relative;
    width: 851px;
    height: 1200px;
    overflow: hidden;
    background:
      radial-gradient(ellipse 70% 45% at 50% 48%, var(--paper) 0%, rgba(248,251,255,0.6) 45%, rgba(248,251,255,0) 80%),
      linear-gradient(160deg, var(--sky-soft) 0%, var(--paper) 35%, var(--sky-soft) 65%, var(--sky-deep) 100%);
  }
  .service-type {
    position: absolute;
    top: 118px;
    left: 0;
    width: 100%;
    margin: 0;
    text-align: center;
    font-size: 46px;
    font-weight: 800;
    color: var(--leaf);
    letter-spacing: 2px;
  }
  .title-glow {
    position: absolute;
    left: 80px;
    top: 225px;
    width: 700px;
    height: 170px;
    border-radius: 50%;
    background: radial-gradient(ellipse at center, var(--leaf-glow) 0%, rgba(184,236,138,0.75) 45%, rgba(184,236,138,0) 72%);
  }
  .facility-name {
    position: absolute;
    top: 232px;
    left: 0;
    width: 100%;
    margin: 0;
    text-align: center;
    font-size: 120px;
    font-weight: 900;
    line-height: 1.2;
    color: var(--leaf-dark);
    -webkit-text-stroke: 10px #ffffff;
    paint-order: stroke fill;
    letter-spacing: 4px;
  }
  .tagline-cloud {
    position: absolute;
    left: 90px;
    top: 445px;
    width: 590px;
    height: 115px;
  }
  .tagline {
    position: absolute;
    left: 90px;
    top: 466px;
    width: 590px;
    margin: 0;
    text-align: center;
    font-size: 48px;
    font-weight: 800;
    color: #ffffff;
  }
  .support-tag {
    position: absolute;
    left: 420px;
    top: 594px;
    width: 330px;
    height: 52px;
    background: var(--tag);
    color: #ffffff;
    font-size: 36px;
    font-weight: 800;
    line-height: 52px;
    text-align: center;
    letter-spacing: 2px;
  }
  .phone {
    position: absolute;
    top: 688px;
    left: 0;
    width: 100%;
    margin: 0;
    text-align: center;
    font-size: 92px;
    font-weight: 900;
    color: var(--phone);
    -webkit-text-stroke: 8px var(--phone-edge);
    paint-order: stroke fill;
    letter-spacing: 2px;
  }
  .art {
    position: absolute;
  }
  .art-blossom-left {
    left: 55px;
    top: 30px;
    width: 110px;
    height: 120px;
    border-radius: 50%;
    background: radial-gradient(circle, var(--blossom) 0%, rgba(246,169,199,0.35) 65%, rgba(246,169,199,0) 100%);
  }
  .art-blossom-right {
    left: 745px;
    top: 180px;
    width: 50px;
    height: 50px;
    border-radius: 50%;
    background: radial-gradient(circle, var(--blossom) 0%, rgba(246,169,199,0) 100%);
  }
  .art-notes {
    left: 690px;
    top: 392px;
    width: 100px;
    height: 46px;
    border-radius: 20px;
    background: linear-gradient(90deg, rgba(238,79,151,0.55), rgba(238,79,151,0.25));
  }
  .art-children-piano {
    left: 60px;
    top: 825px;
    width: 460px;
    height: 300px;
    border-radius: 24px;
    background: linear-gradient(180deg, rgba(244,198,74,0.55) 0%, rgba(244,198,74,0.35) 55%, rgba(127,163,221,0.55) 100%);
  }
  .art-flowers {
    left: 575px;
    top: 855px;
    width: 250px;
    height: 310px;
    border-radius: 24px;
    background: linear-gradient(180deg, rgba(244,198,74,0.6) 0%, rgba(238,79,151,0.3) 50%, rgba(63,155,47,0.45) 100%);
  }
</style>
</head>
<body>
<main class="sign">
  <div class="art art-blossom-left" role="img" aria-label="桜の花のイラスト"></div>
  <div class="art art-blossom-right" role="img" aria-label="小さな桜の花のイラスト"></div>

  <p class="service-type">放課後等デイサービス</p>

  <div class="title-glow"></div>
  <h1 class="facility-name">星のクルミ</h1>

  <div class="art art-notes" role="img" aria-label="ピンクの音符のイラスト"></div>

  <svg class="tagline-cloud" viewBox="0 0 620 120" preserveAspectRatio="none" aria-hidden="true">
    <path d="M40 92 C5 92 5 55 40 52 C42 25 85 18 105 35 C125 8 175 10 190 32 C215 5 270 8 285 30 C310 5 365 8 380 30 C405 8 460 10 470 35 C500 15 550 25 552 52 C600 52 605 95 565 98 C540 118 480 112 470 100 C440 118 390 115 375 102 C345 118 295 116 280 102 C250 118 200 116 185 102 C155 118 100 116 90 100 C70 112 45 108 40 92 Z" fill="var(--cloud)"/>
    <path d="M70 45 C95 30 140 30 160 40" stroke="var(--cloud-light)" stroke-width="6" fill="none" stroke-linecap="round"/>
  </svg>
  <p class="tagline">音楽療育に特化した</p>

  <div class="support-tag">児童発達支援</div>

  <p class="phone">048-372-9051</p>

  <div class="art art-children-piano" role="img" aria-label="鍵盤の上で音符と遊ぶ子どもたちのイラスト"></div>
  <div class="art art-flowers" role="img" aria-label="黄色とピンクの花のイラスト"></div>
</main>
</body>
</html>
```